Lumorax Helpdesk overview brochure

Take the word document that is attached and turn it into a brochure. (Thinking one page, front and back.) the only existing branding/colors we have is the logo that is on the document. It may require a phone all or a bit of back and forth in text to explain some of the concepts in the attached document.

Target Market(s)

Call centers

Industry/Entity Type

It Service

Font styles to use
Sans Serif

Colors

Designer to choose colors to be used in the design.

Requirements
Must have
• A crisp professional look

```html
<!DOCTYPE html>
<html lang="en">
<head>
<meta charset="utf-8">
<title>Lumorax Helpdesk – Overview Brochure</title>
<link href="https://fonts.googleapis.com/css2?family=Open+Sans:wght@400;600;700&family=Roboto+Slab:wght@500;700&family=Source+Sans+3:wght@400;600&display=swap" rel="stylesheet">
<style>
:root{
  --brand:#27a7e1;
  --brand-dark:#1f8fc4;
  --steel:#5b95b8;
  --ink:#3a3a3a;
  --muted:#6b6b6b;
  --line:#c9c9c9;
  --panel:#f4f4f4;
  --cell:#ececec;
  --stage:#e6e6e6;
  --white:#ffffff;
}
*{box-sizing:border-box;margin:0;padding:0}
html,body{width:941px;height:1200px;overflow:hidden}
body{background:var(--stage);font-family:"Open Sans",Arial,sans-serif;color:var(--ink);position:relative}
.spread{position:absolute;background:var(--white);box-shadow:2px 3px 6px rgba(0,0,0,.25);overflow:hidden}
.spread--inside{left:39px;top:31px;width:858px;height:555px}
.spread--outside{left:39px;top:615px;width:851px;height:551px}

/* inside spread */
.right-page{position:absolute;left:431px;top:0;width:427px;height:555px;background:var(--panel)}
.hero-band{position:absolute;left:0;top:33px;width:858px;height:100px}
.hero-band svg{position:absolute;left:0;top:0}
.hero-copy{position:absolute;left:204px;top:54px;width:215px;font-family:"Roboto Slab",Georgia,serif;font-weight:700;font-size:9.3px;line-height:12.6px;color:var(--white)}
.hero-photo{position:absolute;left:0;top:0}

.trends-card{position:absolute;left:18px;top:14px;width:170px;height:525px;background:var(--white);border:1px solid var(--line);border-radius:8px}
.trends-title{position:absolute;left:23px;top:52px;font-family:"Roboto Slab",Georgia,serif;font-weight:700;font-size:13px;line-height:17px;color:var(--brand)}
.trend{position:absolute;left:17px;width:140px}
.trend-head{display:flex;align-items:center;gap:6px;font-size:6.6px;font-weight:700;line-height:8px;color:var(--ink);margin-bottom:7px}
.trend-head svg{flex:none}
.trend p{font-size:6.5px;line-height:11.2px;color:var(--ink)}

.cost-box{position:absolute;top:154px;width:70px;height:68px;border:1.5px solid #9a9a9a;border-radius:8px;background:var(--white)}
.cost-box .ico{position:absolute;left:50%;top:-14px;transform:translateX(-50%)}
.cost-box p{position:absolute;left:4px;right:4px;top:29px;font-size:6.3px;line-height:8px;font-style:italic;text-align:center;color:var(--ink)}
.cost-note{position:absolute;left:204px;top:232px;width:210px;text-align:center;font-size:5.8px;font-style:italic;color:var(--ink)}

.channel-art{position:absolute;left:196px;top:236px}
.channel-box{position:absolute;left:198px;top:317px;width:218px;height:120px;border:1.5px solid var(--brand);border-radius:9px;background:var(--white)}
.channel-grid{position:absolute;left:14px;top:13px;display:grid;grid-template-columns:repeat(4,30px);column-gap:22px;row-gap:20px}
.app{width:30px;height:30px;border-radius:7px;display:flex;align-items:center;justify-content:center;font-size:5.4px;font-weight:700;color:var(--white)}
.app--light{background:#f0f0f0;color:var(--ink)}
.channel-box::after{content:"";position:absolute;left:102px;bottom:-6px;border:5px solid transparent;border-top-color:var(--brand);border-bottom:0}

.savings{position:absolute;left:205px;top:461px;width:198px;height:69px;background:var(--brand)}
.savings svg{position:absolute;left:12px;top:17px}
.savings p{position:absolute;left:61px;top:12px;width:130px;font-family:"Roboto Slab",Georgia,serif;font-weight:700;font-size:7.7px;line-height:10.2px;color:var(--white)}

.engage-title{position:absolute;right:30px;top:163px;font-family:"Roboto Slab",Georgia,serif;font-weight:700;font-size:13.5px;letter-spacing:.3px;color:var(--brand)}
.engage-row{position:absolute;left:454px;width:378px}
.engage-label{position:absolute;left:0;top:0;bottom:0;width:83px;background:var(--brand);color:var(--white);font-size:6.8px;font-weight:700;display:flex;align-items:center;justify-content:center;text-align:center;line-height:8.5px}
.engage-label::after{content:"";position:absolute;right:-9px;top:50%;margin-top:-4px;border:4px solid transparent;border-left:5px solid var(--brand)}
.engage-body{position:absolute;left:88px;top:0;bottom:0;right:0;background:var(--cell);padding:0 14px 0 20px;display:flex;flex-direction:column;justify-content:center;font-size:6.9px;line-height:9.5px;color:var(--ink)}
.engage-body ul{list-style:none}
.engage-body li{padding-left:7px;text-indent:-7px;line-height:12.4px}
.engage-body li.wrap{line-height:9px;padding-top:2px;padding-bottom:2px}
.engage-body li::before{content:"• "}

/* outside spread */
.contact-panel{position:absolute;left:0;top:0;width:426px;height:373px;background:var(--steel)}
.contact{position:absolute;left:0;width:426px;text-align:center;color:var(--white);font-family:"Source Sans 3",Arial,sans-serif;font-size:13.5px;letter-spacing:.6px}
.contact svg{display:block;margin:0 auto 8px}
.tagline{position:absolute;left:445px;top:38px;width:386px;text-align:center;font-family:"Source Sans 3",Arial,sans-serif;font-weight:600;font-size:13.4px;line-height:18.4px;letter-spacing:.4px;color:var(--brand)}
.cover-photo{position:absolute;left:426px;top:95px;width:425px;height:278px;background:linear-gradient(110deg,#f3e8d6 0%,#e9d3b2 30%,#c98a6a 55%,#c6362f 72%,#8a5a3a 100%)}
.stripe{position:absolute;left:0;width:851px;background:var(--brand)}
.stripe--mid{top:373px;height:8px}
.stripe--foot{top:541px;height:10px}
.brand-lockup{position:absolute;display:flex;align-items:center;gap:12px}
.brand-lockup span{font-family:"Roboto Slab",Georgia,serif;font-weight:500;color:var(--brand);line-height:1}
.brand-lockup--back{left:104px;top:424px}
.brand-lockup--back span{font-size:27px}
.brand-lockup--front{left:482px;top:418px}
.brand-lockup--front span{font-size:32px}
.slogan{position:absolute;left:40px;top:507px;width:346px;text-align:center;font-family:"Source Sans 3",Arial,sans-serif;font-weight:600;font-size:12px;letter-spacing:1.6px;color:var(--ink)}
.cover-url{position:absolute;right:38px;top:506px;font-family:"Source Sans 3",Arial,sans-serif;font-weight:600;font-size:12.5px;letter-spacing:.5px;color:var(--ink)}
</style>
</head>
<body>

<section class="spread spread--inside">
  <div class="right-page"></div>

  <div class="hero-band">
    <svg width="858" height="100" viewBox="0 0 858 100" aria-hidden="true">
      <polygon points="0,0 640,0 590,100 0,100" fill="#27a7e1"/>
      <rect x="360" y="-10" width="230" height="120" rx="34" fill="#5cc1ee" transform="rotate(14 475 50)"/>
    </svg>
    <svg class="hero-photo" width="858" height="100" viewBox="0 0 858 100" role="img" aria-label="Photo of a smiling support agent wearing a headset">
      <defs><linearGradient id="agentTone" x1="0" x2="1"><stop offset="0" stop-color="#e9e9ea"/><stop offset=".45" stop-color="#b58f79"/><stop offset=".7" stop-color="#3b2c27"/><stop offset="1" stop-color="#dfe2e6"/></linearGradient></defs>
      <polygon points="651,0 858,0 858,100 601,100" fill="url(#agentTone)"/>
      <polygon points="640,0 651,0 601,100 590,100" fill="#ffffff"/>
    </svg>
  </div>
  <p class="hero-copy">Lumorax Helpdesk will help you shift some traffic from higher cost telephone calls to lower cost messaging channels. Shaping your traffic into lower cost channels has great financial benefits.</p>

  <aside class="trends-card">
    <h2 class="trends-title">New Trends In<br>Customer Service</h2>

    <div class="trend" style="top:121px">
      <div class="trend-head">
        <svg width="24" height="20" viewBox="0 0 24 20" aria-hidden="true"><circle cx="12" cy="10" r="5" fill="#8a8a8a"/><g stroke="#8a8a8a" stroke-width="1.5"><line x1="12" y1="0" x2="12" y2="3"/><line x1="12" y1="17" x2="12" y2="20"/><line x1="2" y1="10" x2="5" y2="10"/><line x1="19" y1="10" x2="22" y2="10"/><line x1="5" y1="3" x2="7" y2="5"/><line x1="17" y1="15" x2="19" y2="17"/><line x1="19" y1="3" x2="17" y2="5"/><line x1="5" y1="17" x2="7" y2="15"/></g></svg>
        <span>Service Through New<br>Channels</span>
      </div>
      <p>The huge popularity of social media and messaging is creating customer preferences to communicate with your company using SMS text messaging, Chatlane, Huddlebox, Voxa, Echoly, Hearthhub, and many other new channels.</p>
    </div>

    <div class="trend" style="top:248px">
      <div class="trend-head">
        <svg width="24" height="22" viewBox="0 0 24 22" aria-hidden="true"><rect x="6" y="1" width="11" height="19" rx="2" fill="none" stroke="#8a8a8a" stroke-width="1.5"/><rect x="8" y="4" width="7" height="11" fill="#8a8a8a"/><path d="M14 14 q6 0 6 6" fill="none" stroke="#8a8a8a" stroke-width="2"/></svg>
        <span>Avoiding App Fatigue</span>
      </div>
      <p>App fatigue has set in. Customers are weary of installing, updating and learning how to use mobile apps. Your customers want to communicate with you using their messaging service of choice or just talk into their smart phone, computer, Echoly or similar device.</p>
    </div>

    <div class="trend" style="top:392px">
      <div class="trend-head">
        <svg width="24" height="22" viewBox="0 0 24 22" aria-hidden="true"><rect x="3" y="2" width="18" height="5" rx="1.5" fill="#8a8a8a"/><rect x="3" y="8.5" width="18" height="5" rx="1.5" fill="#8a8a8a"/><line x1="12" y1="14" x2="12" y2="19" stroke="#8a8a8a" stroke-width="1.5"/><line x1="6" y1="20" x2="18" y2="20" stroke="#8a8a8a" stroke-width="1.5"/></svg>
        <span>Implementing Automation</span>
      </div>
      <p>Sensible automation of customer interactions on these new channels can provide better service at even lower costs of operation. According to Hollisfield's report, by 2020, 85% of customer interactions will be managed without a human.</p>
    </div>
  </aside>

  <div class="cost-box" style="left:197px">
    <svg class="ico" width="28" height="28" viewBox="0 0 28 28" aria-hidden="true"><circle cx="14" cy="14" r="13" fill="#8a8a8a" stroke="#fff" stroke-width="1.5"/><path d="M7 12 q7-6 14 0 l-2 2 -2-1 v-2 q-3-1 -6 0 v2 l-2 1 z" fill="#fff"/><rect x="10" y="14" width="8" height="5" rx="1" fill="#fff"/></svg>
    <p>A telephone call with a live agent. Average cost per call is $17*</p>
  </div>
  <div class="cost-box" style="left:271px">
    <svg class="ico" width="28" height="28" viewBox="0 0 28 28" aria-hidden="true"><circle cx="14" cy="14" r="13" fill="#8a8a8a" stroke="#fff" stroke-width="1.5"/><rect x="7" y="9" width="14" height="10" fill="none" stroke="#fff" stroke-width="1.4"/><path d="M7 9 l7 6 7-6" fill="none" stroke="#fff" stroke-width="1.4"/></svg>
    <p>An email with a live agent. Average cost per email is $15*</p>
  </div>
  <div class="cost-box" style="left:345px">
    <svg class="ico" width="28" height="28" viewBox="0 0 28 28" aria-hidden="true"><circle cx="14" cy="14" r="13" fill="#8a8a8a" stroke="#fff" stroke-width="1.5"/><path d="M7 8 h14 v9 h-8 l-4 3 v-3 h-2 z" fill="#fff"/><g fill="#8a8a8a"><circle cx="10.5" cy="12.5" r="1"/><circle cx="14" cy="12.5" r="1"/><circle cx="17.5" cy="12.5" r="1"/></g></svg>
    <p>A webchat with a live agent. Average cost per web chat is $12*</p>
  </div>
  <p class="cost-note">*Above costs are cited from an Norvale research paper</p>

  <svg class="channel-art" width="240" height="85" viewBox="0 0 240 85" aria-hidden="true">
    <path d="M26 34 q6 24 30 44" fill="none" stroke="#9a9a9a" stroke-width="9"/>
    <polygon points="44,82 70,86 58,62" fill="#9a9a9a"/>
    <path d="M216 34 q-6 24 -30 44" fill="none" stroke="#9a9a9a" stroke-width="9"/>
    <polygon points="198,82 172,86 184,62" fill="#9a9a9a"/>
    <circle cx="109" cy="57" r="24" fill="none" stroke="#4a4a4a" stroke-width="2.5"/>
    <circle cx="109" cy="57" r="14" fill="#27a7e1"/>
  </svg>

  <div class="channel-box">
    <div class="channel-grid">
      <div class="app app--light">Hearthhub</div>
      <div class="app app--light">Pingo</div>
      <div class="app" style="background:#1f8fc4">Echoly</div>
      <div class="app" style="background:#4a7fd8">Chatlane</div>
      <div class="app" style="background:#3cb34a">Talkwave</div>
      <div class="app" style="background:#2f9e44">Quikchat</div>
      <div class="app app--light">SMS</div>
      <div class="app app--light">Huddlebox</div>
    </div>
  </div>

  <div class="savings">
    <svg width="40" height="36" viewBox="0 0 40 36" aria-hidden="true"><circle cx="13" cy="21" r="12" fill="#fff"/><text x="13" y="27" text-anchor="middle" font-family="Arial, sans-serif" font-weight="700" font-size="16" fill="#27a7e1">$</text><circle cx="31" cy="5" r="4" fill="#fff"/><rect x="27" y="10" width="8" height="16" rx="2" fill="#fff"/><rect x="28" y="26" width="2.5" height="9" fill="#fff"/><rect x="31.5" y="26" width="2.5" height="9" fill="#fff"/></svg>
    <p>With these new channels, the cost is similar to webchat. Carefully automated interactions are at an even lower cost...</p>
  </div>

  <h2 class="engage-title">ENGAGEMENT MODEL</h2>

  <div class="engage-row" style="top:183px;height:48px">
    <div class="engage-label">PROPOSAL</div>
    <div class="engage-body">Lumorax Helpdesk provides a written proposal that describes our engagement methodology, costs, and report content.</div>
  </div>
  <div class="engage-row" style="top:234px;height:137px">
    <div class="engage-label">ANALYSIS</div>
    <div class="engage-body">
      <p>Lumorax Helpdesk will meet with all the stakeholders to identify:</p>
      <ul>
        <li>Historical traffic patterns</li>
        <li>Actual costs of services per channel</li>
        <li>Review marketing plans that may impact customer service</li>
        <li>Review product plans that may impact customer service</li>
        <li>Explore the competitive landscape as it relates to customer service</li>
        <li>Review the existing corporate data store, analytics and reporting</li>
        <li class="wrap">Review the current plans, metrics and budgets for customer service support</li>
      </ul>
    </div>
  </div>
  <div class="engage-row" style="top:374px;height:159px">
    <div class="engage-label">TRANSFORMATION<br>REPORT</div>
    <div class="engage-body">
      <ul>
        <li>Executive summary</li>
        <li>Cost analysis by channel</li>
        <li>Traffic patterns by channel</li>
        <li>Probable impacts of product and marketing plans</li>
        <li class="wrap">Recommendations for achieving competitive advantage through service</li>
        <li>Recommendations for new channel types</li>
        <li>Recommendations for traffic shaping</li>
        <li>Near and long-term options for sensible automation</li>
        <li>Technology recommendations for implementing new channels</li>
        <li>Projected financial impact of recommendations</li>
      </ul>
    </div>
  </div>
</section>

<section class="spread spread--outside">
  <div class="contact-panel">
    <div class="contact" style="top:63px">
      <svg width="38" height="38" viewBox="0 0 38 38" aria-hidden="true"><circle cx="19" cy="19" r="17.5" fill="none" stroke="#fff" stroke-width="2"/><path d="M10 17 q9-8 18 0 l-3 3 -2.5-1.5 v-2 q-3.5-1.5 -7 0 v2 l-2.5 1.5 z" fill="#fff"/><ellipse cx="19" cy="22" rx="5" ry="3" fill="#fff"/></svg>
      555-014-2290
    </div>
    <div class="contact" style="top:159px">
      <svg width="38" height="38" viewBox="0 0 38 38" aria-hidden="true"><circle cx="19" cy="19" r="17.5" fill="none" stroke="#fff" stroke-width="2"/><rect x="10" y="13" width="18" height="12" fill="#fff"/><path d="M10 13 l9 7 9-7" fill="none" stroke="#5b95b8" stroke-width="1.5"/></svg>
      sales@lumoraxhelpdesk.net
    </div>
    <div class="contact" style="top:255px">
      <svg width="38" height="38" viewBox="0 0 38 38" aria-hidden="true"><circle cx="19" cy="19" r="17.5" fill="none" stroke="#fff" stroke-width="2"/><circle cx="19" cy="19" r="9" fill="#fff"/><path d="M11 16 q8 3 16 0 M12 23 q7-2 14 1 M19 10 q-4 9 0 18" fill="none" stroke="#5b95b8" stroke-width="1.3"/></svg>
      www.lumoraxhelpdesk.net
    </div>
  </div>

  <p class="tagline">Helping Contact Centers Serve New Customer Access Channels, Improve Customer Service, and Lower Costs of Operation</p>
  <div class="cover-photo" role="img" aria-label="Photo of a young woman in a red coat using her phone outdoors"></div>

  <div class="stripe stripe--mid"></div>

  <div class="brand-lockup brand-lockup--back">
    <svg width="58" height="58" viewBox="0 0 58 58" aria-hidden="true"><circle cx="29" cy="29" r="26" fill="none" stroke="#27a7e1" stroke-width="3"/></svg>
    <span>Lumorax<br>Helpdesk</span>
  </div>
  <p class="slogan">THE NEXT LEAP FORWARD IN CUSTOMER SERVICE</p>

  <div class="brand-lockup brand-lockup--front">
    <svg width="70" height="70" viewBox="0 0 70 70" aria-hidden="true"><circle cx="35" cy="35" r="32" fill="none" stroke="#27a7e1" stroke-width="3"/></svg>
    <span>Lumorax<br>Helpdesk</span>
  </div>
  <p class="cover-url">www.lumoraxhelpdesk.net</p>

  <div class="stripe stripe--foot"></div>
</section>

</body>
</html>
```